Voice agent website redesign, responsive. Current website functional, needs fresh look.

** updated 01/04/2015 ** Stock photos and video OK
Tal Studios is redesigning their website to refresh the look and feel and also to make the website more useable in portable devices.
We also intend to replace our existing iPhone app with responsive HTML.
We want to keep the features but update the way they are displayed.
The current website is at: http://www.talstudios.com.au. (examples of important pages are in the attachments)
The current website is written in .NET and MS SQL but designs optimised for WordPress will also be accepted.
We have corporate colours and a logo
We want a dynamic element on the front page
We do not mind the idea of a slider, but I must be modern and capable of video backgrounds
We like the clean design of our main competitor: http://www.pwd.com.au but the site is busy and not responsive.
The site must be designed to use responsive HTML and be easy to see and navigate using smaller viewports.
Once awarded the contract the designer must supply 4 pages in 3 formats, for which we will pay an extra $80, as outlined below:
Submission for selection
Designs must be submitted for selection with 1 required page (home page) in 1 required resolution and 1 optional resolution;
Versions:
• (Required) Full page web landscape – 1920 x 1080
• (Optional) Low resolution portrait (e.g. iPhone 3/4) – 320 x 480
Submission required when awarded
Final supplied designs must have 3 versions of 4 required pages as layered Photoshop files;
Versions:
• Full page web landscape – 1920 x 1080
• Medium resolution landscape (e.g. iPad) – 1024 x 768
• Low resolution portrait (e.g. iPhone 3/4) – 320 x 480
Pages:
• home page
• generic template
• search results
• talent page
The designer may also offer to convert the site into HTML and CSS for an added fee.
The attachments supplied contains important features like site menu and required elements, but only guidelines to design.
Please do read carefully for details on required elements, but do feel free to change the design, look and feel completely.
Attached are;
Advertising agencies who hire voice artists, also a showcase for the artists themselves

```html
<!DOCTYPE html>
<html lang="en">
<head>
<meta charset="utf-8">
<title>Tal Studios – Voice Over Artists</title>
<link href="https://fonts.googleapis.com/css2?family=Montserrat:wght@400;600;700&family=Open+Sans:ital,wght@0,400;0,600;0,700;1,400&display=swap" rel="stylesheet">
<style>
:root{
  --navy:#0c2b4d;
  --navy-deep:#08203b;
  --green:#7bbf2a;
  --grey-bg:#efefef;
  --text:#333;
  --muted:#9a9a9a;
  --white:#fff;
  --line:#d8d8d8;
}
*{box-sizing:border-box;margin:0;padding:0}
html,body{width:1200px;height:3340px;overflow:hidden}
body{font-family:"Open Sans",Arial,sans-serif;color:var(--text);background:var(--white);position:relative}
section,header,footer{position:absolute;left:0;width:1200px}
.heading{font-family:"Montserrat",Arial,sans-serif;font-weight:700;font-size:21px;color:var(--navy);text-align:center;letter-spacing:.3px}
.intro{font-size:12.5px;line-height:20px;color:var(--muted);text-align:center}
.pill{display:inline-block;border-radius:16px;font-family:"Montserrat",Arial,sans-serif;font-weight:700;font-size:11px;color:var(--white);text-align:center;line-height:31px;text-transform:uppercase}
.pill--navy{background:var(--navy)}
.pill--green{background:var(--green)}
.arrow{position:absolute;width:32px;height:32px}

/* Hero */
.hero{top:0;height:597px;background:linear-gradient(120deg,#3d3a37 0%,#6b5a4c 30%,#4a3e38 55%,#7a5d4a 75%,#2f2b2a 100%)}
.hero__photo{position:absolute;inset:0;background:radial-gradient(ellipse at 30% 50%,rgba(160,120,90,.45),transparent 60%),radial-gradient(ellipse at 75% 40%,rgba(140,90,70,.4),transparent 55%);}
.hero__shade{position:absolute;inset:0;background:rgba(20,20,25,.35)}
.site-header{top:0;height:82px;background:rgba(8,32,59,.9);z-index:2}
.logo{position:absolute;left:98px;top:18px;display:flex;align-items:center;gap:10px;font-family:"Montserrat",Arial,sans-serif;font-weight:700;font-size:26px;color:var(--white)}
.logo__mark{width:22px;height:22px;background:var(--green)}
.nav{position:absolute;left:347px;top:0;display:flex;height:82px}
.nav a{font-family:"Montserrat",Arial,sans-serif;font-size:12.5px;color:var(--white);text-decoration:none;line-height:82px;padding:0 20px}
.nav a.is-active{background:var(--green)}
.header-phone{position:absolute;left:936px;top:22px;display:flex;gap:14px;align-items:center}
.header-phone__numbers{font-family:"Montserrat",Arial,sans-serif;font-size:14px;color:var(--green);line-height:20px;font-weight:600}
.hero__copy{position:absolute;top:230px;width:100%;text-align:center;color:var(--white)}
.hero__title{font-family:"Montserrat",Arial,sans-serif;font-weight:700;font-size:44px;letter-spacing:.5px}
.hero__sub{font-family:"Montserrat",Arial,sans-serif;font-size:26px;line-height:33px;margin-top:14px}
.hero__play{position:absolute;left:570px;top:400px}
.search-tab{position:absolute;left:98px;top:546px;width:285px;height:51px;background:var(--green);color:var(--white);font-family:"Montserrat",Arial,sans-serif;font-weight:700;font-size:20px;line-height:51px;padding-left:20px}
.search-tab svg{position:absolute;right:18px;top:17px}

/* Search */
.search{top:597px;height:173px;background:var(--grey-bg)}
.search__fields{position:absolute;left:98px;top:22px;display:flex;gap:11px}
.field__label{font-size:11px;color:#444;text-transform:uppercase;height:24px}
.field__select{height:36px;background:var(--white);border:1px solid #e2e2e2;font-size:12px;color:#666;line-height:34px;padding-left:8px;position:relative}
.field__select::after{content:"";position:absolute;right:0;top:0;width:22px;height:34px;background:#e6e6e6}
.search__actions{position:absolute;left:98px;top:118px;display:flex;gap:11px}

/* Recent work */
.recent{top:770px;height:401px;background:var(--white)}
.cards{position:absolute;left:138px;display:flex;gap:10px}
.work-card{width:224px;background:#eee}
.work-card__media{height:156px;position:relative}
.work-card__media svg{position:absolute;left:92px;top:58px}
.work-card__name{height:42px;line-height:42px;text-align:center;font-size:12.5px;color:#555}

/* News */
.news{top:1171px;height:455px;background:var(--green)}
.news .heading{color:var(--white)}
.news .intro{color:#eef6e0}
.news__cards{position:absolute;left:138px;top:136px;display:flex;gap:19px}
.news-card{width:169px;height:261px;background:var(--white);border-radius:3px;padding:11px;text-align:center}
.news-card__media{height:103px}
.news-card__name{font-size:12.5px;color:#333;margin-top:16px}
.news-card__date{font-size:10.5px;color:var(--navy);font-weight:600;margin-top:10px}
.news-card__text{font-size:10.5px;color:#888;line-height:16px;margin-top:10px}

/* Spotlight */
.spotlight{top:1626px;height:461px;background:var(--white)}
.spot-card{width:224px;text-align:center}
.spot-card__media{height:156px}
.spot-card__name{font-size:12.5px;color:#444;margin-top:18px}
.spot-card__text{font-size:10.5px;color:#888;line-height:18px;margin-top:10px}
.spot-card .pill{width:84px;line-height:30px;font-size:10px;margin-top:13px}

/* Dynamic */
.dynamic{top:2087px;height:396px;background:var(--navy)}
.dynamic .heading{color:var(--green)}
.dynamic .intro{color:#e1e7ee}
.dyn-card{position:absolute;top:142px;width:223px;background:var(--white)}
.dyn-card__media{height:156px}
.dyn-card__name{height:43px;line-height:43px;text-align:center;font-size:12.5px;color:#555;background:#f1f1f1}

/* Testimonials */
.testimonials{top:2483px;height:348px;background:var(--white)}
.testimonials .intro{font-style:italic;font-size:11.5px;line-height:22px;color:#999}
.client{position:absolute;top:163px;width:120px;text-align:center}
.client__photo{width:98px;height:98px;border-radius:50%;margin:0 auto;border:3px solid #e4e4e4}
.client__name{font-size:12px;color:#444;line-height:18px;margin-top:12px}

/* Ready */
.ready{top:2831px;height:205px;background:var(--grey-bg)}

/* Footer */
.site-footer{top:3036px;height:244px;background:var(--white)}
.footer-col{position:absolute;top:46px}
.footer-col__title{font-family:"Montserrat",Arial,sans-serif;font-size:14px;color:#222;margin-bottom:14px;text-transform:uppercase}
.footer-col p,.footer-col li{font-size:11.5px;color:#444;line-height:22px;list-style:none}
.footer-divider{position:absolute;top:46px;width:1px;height:170px;background:var(--line)}
.newsletter__form{display:flex;margin-top:10px}
.newsletter__input{width:214px;height:42px;background:#eee;font-size:11.5px;color:#999;line-height:42px;padding-left:12px}
.newsletter__go{width:46px;height:42px;background:var(--navy);color:var(--white);font-family:"Montserrat",Arial,sans-serif;font-weight:700;font-size:12px;text-align:center;line-height:42px}
.follow{display:flex;align-items:center;gap:9px;margin-top:16px;font-family:"Montserrat",Arial,sans-serif;font-size:15px;color:var(--navy);font-weight:600}
.follow__icon{width:33px;height:33px;background:var(--green)}
.copyright{top:3280px;height:60px;background:var(--navy-deep);color:#d5dbe3;font-size:11px;text-align:center;line-height:60px}
</style>
</head>
<body>

<section class="hero" aria-label="Hero">
  <div class="hero__photo" role="img" aria-label="Video background of a group of smiling friends talking outdoors"></div>
  <div class="hero__shade"></div>
  <div class="hero__copy">
    <h1 class="hero__title">JUST SAY THE WORD</h1>
    <p class="hero__sub">Australia's top voice over artists.<br>Professional voice casting Service.</p>
  </div>
  <svg class="hero__play" width="60" height="60" viewBox="0 0 60 60" aria-label="Play video"><circle cx="30" cy="30" r="27" fill="none" stroke="#fff" stroke-width="3"/><path d="M24 19 L41 30 L24 41 Z" fill="#fff"/></svg>
  <div class="search-tab">SEARCH OUR ARTISTS
    <svg width="12" height="16" viewBox="0 0 12 16"><path d="M1 1 L11 8 L1 15 Z" fill="#fff"/></svg>
  </div>
</section>

<header class="site-header">
  <div class="logo"><span>Tal Studios</span><span class="logo__mark"></span></div>
  <nav class="nav">
    <a class="is-active">HOME</a><a>RATES</a><a>ABOUT US</a><a>PAYMENTS</a><a>SHORTLIST</a><a>CONTACT</a>
  </nav>
  <div class="header-phone">
    <svg width="24" height="22" viewBox="0 0 24 22" aria-label="Phone"><path d="M2 8 Q12 0 22 8 L19 11 L16 9 L16 6 Q12 4 8 6 L8 9 L5 11 Z" fill="#7bbf2a"/><rect x="5" y="12" width="14" height="9" rx="2" fill="#7bbf2a"/></svg>
    <div class="header-phone__numbers">+61 2 5550 1200<br>+61 3 5550 3400</div>
  </div>
</header>

<section class="search" aria-label="Search artists">
  <div class="search__fields">
    <div style="width:185px"><div class="field__label">Search by name</div><div class="field__select">Please Select</div></div>
    <div style="width:151px"><div class="field__label">Location</div><div class="field__select">Any</div></div>
    <div style="width:93px"><div class="field__label">Sex</div><div class="field__select">Any</div></div>
    <div style="width:152px"><div class="field__label">Voice type</div><div class="field__select">Any</div></div>
    <div style="width:93px"><div class="field__label">Age</div><div class="field__select">Any</div></div>
    <div style="width:152px"><div class="field__label">Language</div><div class="field__select">Any</div></div>
    <div style="width:109px"><div class="field__label">Accent</div><div class="field__select">Any</div></div>
  </div>
  <div class="search__actions">
    <span class="pill pill--navy" style="width:85px">View all</span>
    <span class="pill pill--green" style="width:82px">Search</span>
  </div>
</section>

<section class="recent" aria-label="Recent work">
  <h2 class="heading" style="margin-top:38px">RECENT WORK</h2>
  <p class="intro" style="margin-top:8px">Lorem ipsum dolor sit amet, consectetur adipiscing elit. Nulla convallis egestas rhoncus.<br>Donec facilisis fermentum sem, ac viverra ante luctus vel.</p>
  <svg class="arrow" style="left:91px;top:196px" viewBox="0 0 32 32"><circle cx="16" cy="16" r="15" fill="#fff" stroke="#ccc" stroke-width="1.5"/><path d="M19 9 L12 16 L19 23" fill="none" stroke="#bbb" stroke-width="2"/></svg>
  <svg class="arrow" style="left:1077px;top:196px" viewBox="0 0 32 32"><circle cx="16" cy="16" r="15" fill="#fff" stroke="#ccc" stroke-width="1.5"/><path d="M13 9 L20 16 L13 23" fill="none" stroke="#bbb" stroke-width="2"/></svg>
  <div class="cards" style="top:134px">
    <div class="work-card"><div class="work-card__media" role="img" aria-label="Video thumbnail of a small creature on green grass" style="background:linear-gradient(160deg,#9bc45a,#4f7d24)"><svg width="40" height="40" viewBox="0 0 40 40"><circle cx="20" cy="20" r="19" fill="rgba(0,0,0,.45)"/><path d="M16 12 L28 20 L16 28 Z" fill="#fff"/></svg></div><div class="work-card__name">Noah Brennan Kell</div></div>
    <div class="work-card"><div class="work-card__media" role="img" aria-label="Video thumbnail of hands typing on a laptop" style="background:linear-gradient(160deg,#d9b3bd,#8e6874)"><svg width="40" height="40" viewBox="0 0 40 40"><circle cx="20" cy="20" r="19" fill="rgba(0,0,0,.45)"/><path d="M16 12 L28 20 L16 28 Z" fill="#fff"/></svg></div><div class="work-card__name">Noah Brennan Kell</div></div>
    <div class="work-card"><div class="work-card__media" role="img" aria-label="Video thumbnail of a laptop on a desk" style="background:linear-gradient(160deg,#b8b8b2,#6e6a62)"><svg width="40" height="40" viewBox="0 0 40 40"><circle cx="20" cy="20" r="19" fill="rgba(0,0,0,.45)"/><path d="M16 12 L28 20 L16 28 Z" fill="#fff"/></svg></div><div class="work-card__name">Noah Brennan Kell</div></div>
    <div class="work-card"><div class="work-card__media" role="img" aria-label="Video thumbnail of a dog wearing sunglasses by a pool" style="background:linear-gradient(160deg,#5aa7de,#1f5f9e)"><svg width="40" height="40" viewBox="0 0 40 40"><circle cx="20" cy="20" r="19" fill="rgba(0,0,0,.45)"/><path d="M16 12 L28 20 L16 28 Z" fill="#fff"/></svg></div><div class="work-card__name">Noah Brennan Kell</div></div>
  </div>
</section>

<section class="news" aria-label="Latest news">
  <h2 class="heading" style="margin-top:42px">LATEST NEWS</h2>
  <p class="intro" style="margin-top:8px">Lorem ipsum dolor sit amet, consectetur adipiscing elit. Nulla convallis egestas rhoncus.<br>Donec facilisis fermentum sem, ac viverra ante luctus vel.</p>
  <svg class="arrow" style="left:91px;top:250px" viewBox="0 0 32 32"><circle cx="16" cy="16" r="14" fill="none" stroke="#fff" stroke-width="2"/><path d="M19 9 L12 16 L19 23" fill="none" stroke="#fff" stroke-width="2.5"/></svg>
  <svg class="arrow" style="left:1077px;top:250px" viewBox="0 0 32 32"><circle cx="16" cy="16" r="14" fill="none" stroke="#fff" stroke-width="2"/><path d="M13 9 L20 16 L13 23" fill="none" stroke="#fff" stroke-width="2.5"/></svg>
  <div class="news__cards">
    <article class="news-card"><div class="news-card__media" role="img" aria-label="Portrait photo of a man in glasses" style="background:linear-gradient(160deg,#c8c8c8,#8a8a8a)"></div><div class="news-card__name">Noah Brennan Kell</div><div class="news-card__date">March 23 2015</div><p class="news-card__text">Lorem ipsum dolor sit amet, consectetur adipiscing elit. Nulla convallis egestas</p></article>
    <article class="news-card"><div class="news-card__media" role="img" aria-label="Portrait photo of a smiling woman" style="background:linear-gradient(160deg,#f0d2b4,#c38e63)"></div><div class="news-card__name">Noah Brennan Kell</div><div class="news-card__date">March 23 2015</div><p class="news-card__text">Lorem ipsum dolor sit amet, consectetur adipiscing elit. Nulla convallis egestas</p></article>
    <article class="news-card"><div class="news-card__media" role="img" aria-label="Portrait photo of a woman outdoors" style="background:linear-gradient(160deg,#8cbf4e,#d9b48c)"></div><div class="news-card__name">Noah Brennan Kell</div><div class="news-card__date">March 23 2015</div><p class="news-card__text">Lorem ipsum dolor sit amet, consectetur adipiscing elit. Nulla convallis egestas</p></article>
    <article class="news-card"><div class="news-card__media" role="img" aria-label="Portrait photo of a man in glasses" style="background:linear-gradient(160deg,#7db3d8,#3c6f97)"></div><div class="news-card__name">Noah Brennan Kell</div><div class="news-card__date">March 23 2015</div><p class="news-card__text">Lorem ipsum dolor sit amet, consectetur adipiscing elit. Nulla convallis egestas</p></article>
    <article class="news-card"><div class="news-card__media" role="img" aria-label="Portrait photo of a man in a suit" style="background:linear-gradient(160deg,#6d5a4c,#2e2620)"></div><div class="news-card__name">Noah Brennan Kell</div><div class="news-card__date">March 23 2015</div><p class="news-card__text">Lorem ipsum dolor sit amet, consectetur adipiscing elit. Nulla convallis egestas</p></article>
  </div>
</section>

<section class="spotlight" aria-label="Spotlight">
  <h2 class="heading" style="margin-top:34px">SPOTLIGHT</h2>
  <p class="intro" style="margin-top:8px">Lorem ipsum dolor sit amet, consectetur adipiscing elit. Nulla convallis egestas rhoncus.<br>Donec facilisis fermentum sem, ac viverra ante luctus vel.</p>
  <svg class="arrow" style="left:91px;top:195px" viewBox="0 0 32 32"><circle cx="16" cy="16" r="15" fill="#fff" stroke="#ccc" stroke-width="1.5"/><path d="M19 9 L12 16 L19 23" fill="none" stroke="#bbb" stroke-width="2"/></svg>
  <svg class="arrow" style="left:1077px;top:195px" viewBox="0 0 32 32"><circle cx="16" cy="16" r="15" fill="#fff" stroke="#ccc" stroke-width="1.5"/><path d="M13 9 L20 16 L13 23" fill="none" stroke="#bbb" stroke-width="2"/></svg>
  <div class="cards" style="top:129px">
    <div class="spot-card"><div class="spot-card__media" role="img" aria-label="Portrait photo of a smiling young man" style="background:linear-gradient(160deg,#d8b894,#8a6a4c)"></div><div class="spot-card__name">Liam Carter Sydney</div><p class="spot-card__text">Lorem ipsum dolor sit amet, consecte-<br>tur adipiscing elit nulla convallis</p><span class="pill pill--navy">Read more</span></div>
    <div class="spot-card"><div class="spot-card__media" role="img" aria-label="Portrait photo of a woman with dark hair" style="background:linear-gradient(160deg,#e6e6e6,#a9a9a9)"></div><div class="spot-card__name">Noah Brennan Kell</div><p class="spot-card__text">Lorem ipsum dolor sit amet, consecte-<br>tur adipiscing elit nulla convallis</p><span class="pill pill--navy">Read more</span></div>
    <div class="spot-card"><div class="spot-card__media" role="img" aria-label="Photo of a man working at a laptop in an office" style="background:linear-gradient(160deg,#d9e4ee,#5c7890)"></div><div class="spot-card__name">Owen Pryce Brisbane</div><p class="spot-card__text">Lorem ipsum dolor sit amet, consecte-<br>tur adipiscing elit nulla convallis</p><span class="pill pill--navy">Read more</span></div>
    <div class="spot-card"><div class="spot-card__media" role="img" aria-label="Portrait photo of a woman among autumn leaves" style="background:linear-gradient(160deg,#e0a03a,#b5452a)"></div><div class="spot-card__name">Mei-Lin Tan Melbourne</div><p class="spot-card__text">Lorem ipsum dolor sit amet, consecte-<br>tur adipiscing elit nulla convallis</p><span class="pill pill--navy">Read more</span></div>
  </div>
</section>

<section class="dynamic" aria-label="Dynamic element">
  <h2 class="heading" style="margin-top:42px">DYNAMIC ELEMENT</h2>
  <p class="intro" style="margin-top:8px">Lorem ipsum dolor sit amet, consectetur adipiscing elit. Nulla convallis egestas rhoncus.<br>Donec facilisis fermentum sem, ac viverra ante luctus vel.</p>
  <div class="dyn-card" style="left:100px"><div class="dyn-card__media" role="img" aria-label="Portrait photo of a bald man in glasses" style="background:linear-gradient(160deg,#e8e8e8,#9d9d9d)"></div><div class="dyn-card__name">Noah Brennan Kell</div></div>
  <div class="dyn-card" style="left:363px"><div class="dyn-card__media" role="img" aria-label="Portrait photo of a blonde woman" style="background:linear-gradient(160deg,#e9d2b4,#9a7a58)"></div><div class="dyn-card__name">Noah Brennan Kell</div></div>
  <div class="dyn-card" style="left:626px"><div class="dyn-card__media" role="img" aria-label="Portrait photo of a man at the beach" style="background:linear-gradient(160deg,#8fc9e8,#c9a27a)"></div><div class="dyn-card__name">Noah Brennan Kell</div></div>
  <div class="dyn-card" style="left:877px"><div class="dyn-card__media" role="img" aria-label="Portrait photo of a laughing woman" style="background:linear-gradient(160deg,#f2f2f2,#c9a88a)"></div><div class="dyn-card__name">Noah Brennan Kell</div></div>
</section>

<section class="testimonials" aria-label="Client testimonials">
  <h2 class="heading" style="margin-top:38px">CLIENT TESTIMONIALS</h2>
  <p class="intro" style="margin-top:8px">Ullamco laboris dolor sit amet, consectetur adipiscing elit, sed do eiusmod tempor incididunt ut labore et dolore magna aliqua. Ut enim<br>ad minim veniam, quis nostrud exercitation ullamco laborisUllamco laboris dolor sit amet, consectetur adipiscing elit, sed do eiusmod<br>tempor incididunt ut labore et dolore magna aliqua. Ut enim ad minim veniam, quis nostru</p>
  <div class="client" style="left:408px"><div class="client__photo" role="img" aria-label="Round portrait photo of a client" style="background:linear-gradient(160deg,#f1e2d2,#b98e70)"></div><div class="client__name">Noah Brennan<br>Kell</div></div>
  <div class="client" style="left:541px"><div class="client__photo" role="img" aria-label="Round portrait photo of a client" style="background:linear-gradient(160deg,#8ccf3e,#3c6a14)"></div><div class="client__name">Noah Brennan<br>Kell</div></div>
  <div class="client" style="left:668px"><div class="client__photo" role="img" aria-label="Round portrait photo of a client" style="background:linear-gradient(160deg,#d8d8d8,#6a6a6a)"></div><div class="client__name">Noah Brennan<br>Kell</div></div>
</section>

<section class="ready" aria-label="Call to action">
  <h2 class="heading" style="margin-top:38px">ARE YOU READY?</h2>
  <p class="intro" style="margin-top:8px">Lorem ipsum dolor sit amet, consectetur adipiscing elit. Nulla convallis egestas rhoncus.<br>Donec facilisis fermentum sem, ac viverra ante luctus vel.</p>
  <div style="text-align:center;margin-top:14px">
    <span class="pill pill--navy" style="width:85px">Login</span>
    <span class="pill pill--green" style="width:85px;margin-left:6px">Get ready</span>
  </div>
</section>

<footer class="site-footer">
  <div class="footer-col" style="left:98px">
    <h3 class="footer-col__title">Contact us</h3>
    <p>Tal Studios Pty Limited Suite 14 90 Harbour Rd<br>Eastvale NSW 2099 Australia<br>p +61 2 5550 1200<br>p +61 3 5550 3400<br>f +61 2 5550 1299</p>
    <p style="margin-top:10px">Sam Whitford: sam@talstudios.com.au</p>
  </div>
  <div class="footer-divider" style="left:396px"></div>
  <div class="footer-col" style="left:450px">
    <h3 class="footer-col__title">Links</h3>
    <ul><li>HOME</li><li>RATES</li><li>ABOUT US</li><li>FAQS PAYMENTS</li><li>LOGIN</li><li>CONTACT</li></ul>
  </div>
  <div class="footer-divider" style="left:592px"></div>
  <div class="footer-col" style="left:661px">
    <h3 class="footer-col__title">Other</h3>
    <ul><li>Por qué Nosotros?</li><li>Qué hacemos?</li><li>Donantes</li><li>Construcción</li><li>Contacto</li></ul>
  </div>
  <div class="footer-divider" style="left:790px"></div>
  <div class="footer-col" style="left:837px">
    <h3 class="footer-col__title">Newsletter</h3>
    <p style="color:#999">Lorem ipsum dolor sit amet, consectetur adi</p>
    <div class="newsletter__form"><div class="newsletter__input">Email Address:</div><div class="newsletter__go">GO</div></div>
    <div class="follow">FOLLOW
      <span class="follow__icon" role="img" aria-label="Social network link"></span>
      <span class="follow__icon" role="img" aria-label="Social network link"></span>
      <span class="follow__icon" role="img" aria-label="Social network link"></span>
      <span class="follow__icon" role="img" aria-label="Social network link"></span>
    </div>
  </div>
</footer>

<div class="copyright" style="position:absolute;left:0;width:1200px">© Copyright 2015 Tal Studios Pty Limited Privacy Policy &amp; Terms and Conditions</div>

</body>
</html>
```